Borrowed Lanterns - the new thriller in the Tidewater series by award-winning author Marta K. Belloway

Looking for an book cover design for the 4th book in the Tidewater series by Marta K. Belloway. Covers from the first 3 books are attached. Would like to keep a series look going, so possibly using a hand holding a paint brush might work - but not tied down to showing a hand on the cover. Most of the book takes place in a rustic Arizona desert estate in a national forest - so something depicting a desert scene might work too. The cover needs to convey a "thriller" feeling. Attached is our design template with needed specs. Also attached are two other covers for inspiration:

A GARDEN UNDER SALT - something like this could work in the key were a paintbrush and the scene is set in the Arizona desert

THE ORCHARD AT NOON - this could work too with Arizona desert setting

Here's the synopsis of BORROWED LANTERNS:

Her life ended and she is disappointed to discover she is still alive.

With all ties to her handler or anyone connected to her life as a hired killer, she struggles to understand who and even what she has become. She knows she doesn’t want to kill again. And yes, danger finds her and she responds, animal-like, in the only way she knows how.

In this mood of absolute bereavement, she comes across Harriet Vasquell, a world famous artist who has spent the last three decades living a hermit-like existence on a rustic desert estate in a national forest.

Harriet invites her to stay on to assist the old woman who will, in return, mentor our narrator as she deepens her own interest in art.

What is not at first apparent is that elements of Harriet’s past are shrouded in danger, sorrow and darkness and rather than growing as an artist, she soon finds herself enmeshed in a dangerous mystery with strands that stretch decades into the past.

```html
<!DOCTYPE html>
<html lang="en">
<head>
<meta charset="utf-8">
<title>Borrowed Lanterns — Marta K. Belloway</title>
<link rel="stylesheet" href="https://fonts.googleapis.com/css2?family=Bebas+Neue&family=Oswald:wght@300;400&display=swap">
<style>
  :root {
    --page-bg: #e4e4e4;
    --sky-top: #03070f;
    --sky-mid: #0b1c36;
    --horizon: #25608f;
    --ground: #15365c;
    --ground-deep: #081627;
    --ink-light: #f1f1f1;
    --accent-yellow: #e9c400;
  }
  * { margin: 0; padding: 0; box-sizing: border-box; }
  html, body {
    width: 1200px;
    height: 800px;
    overflow: hidden;
    background: var(--page-bg);
  }
  .canvas {
    position: relative;
    width: 1200px;
    height: 800px;
  }
  .book-cover {
    position: absolute;
    left: 400px;
    top: 96px;
    width: 400px;
    height: 608px;
    overflow: hidden;
    border-radius: 2px;
  }
  .cover-art {
    position: absolute;
    inset: 0;
    background:
      radial-gradient(ellipse 70% 12% at 50% 56%, rgba(70, 140, 190, 0.55), transparent 70%),
      linear-gradient(to bottom,
        var(--sky-top) 0%,
        var(--sky-mid) 30%,
        var(--horizon) 52%,
        #1a4570 58%,
        var(--ground) 70%,
        var(--ground-deep) 100%);
  }
  .cover-text {
    position: absolute;
    inset: 0;
    text-align: center;
    color: var(--ink-light);
  }
  .blurb-quote {
    position: absolute;
    top: 24px;
    left: 0;
    right: 0;
    font-family: "Oswald", sans-serif;
    font-weight: 300;
    font-size: 23px;
    letter-spacing: -0.2px;
    line-height: 1;
  }
  .blurb-source {
    position: absolute;
    top: 54px;
    left: 0;
    right: 0;
    font-family: "Oswald", sans-serif;
    font-weight: 300;
    font-size: 13px;
    color: var(--accent-yellow);
    line-height: 1;
  }
  .book-title {
    position: absolute;
    top: 216px;
    left: 0;
    right: 0;
    font-family: "Bebas Neue", sans-serif;
    font-weight: 400;
    font-size: 74px;
    line-height: 74px;
    letter-spacing: 0.14em;
    padding-left: 0.14em;
  }
  .title-line { display: block; }
  .title-line--accent { color: var(--accent-yellow); }
  .book-label {
    position: absolute;
    top: 364px;
    left: 0;
    right: 0;
    font-family: "Oswald", sans-serif;
    font-weight: 300;
    font-size: 24px;
    line-height: 1;
  }
  .book-author {
    position: absolute;
    top: 518px;
    left: 0;
    right: 0;
    font-family: "Bebas Neue", sans-serif;
    font-weight: 400;
    font-size: 56px;
    line-height: 1;
    letter-spacing: -0.5px;
  }
</style>
</head>
<body>
  <main class="canvas">
    <section class="book-cover">
      <div class="cover-art" role="img" aria-label="Night sky with dark storm clouds over a vast cracked, dry desert floor in deep blue tones"></div>
      <div class="cover-text">
        <p class="blurb-quote">“Brilliant. Terrifying. Compulsively readable”</p>
        <p class="blurb-source">-CORINNE ASHWORTH, Harbor City Ledger best-selling author</p>
        <h1 class="book-title">
          <span class="title-line">BORROWED</span>
          <span class="title-line title-line--accent">LANTERNS</span>
        </h1>
        <p class="book-label">A NOVEL</p>
        <p class="book-author">MARTA K. BELLOWAY</p>
      </div>
    </section>
  </main>
</body>
</html>
```